Brochure Cover and Back pages

We are a US-based cosmetics company that sells state-of-the-art skin care products, including advanced anti-aging serums, natural mineral sunscreens, organic antioxidant moisturizers, and organic face cleansers. We need a product brochure. We already have chosen a design for the layout of the product info pages. But we still need a cover page and a back page. We are looking for simple but elegant design for the cover page. The back page is less important and we already know what we want on the back page. It will be the company's mission statement and at the bottom, the company URL, phone number, etc.

The brochure has two folds. So there will be three panels on both sides. The size of each panel is 16.5 (l) x 9.5 (w) cm.

At the end of the project, we expect the designer to integrate all the pages so that the finished copy is read to be sent off to a printing service for printing.

All the product info pages are attached. Also attached are the text (info) to go on the back page, company logo with and without the tagline, the icon in the logo.

YOu are welcome to visit our website www.morvask.com to learn about our products.

Industry/Entity Type

Cosmetics

```html
<!DOCTYPE html>
<html lang="en">
<head>
<meta charset="utf-8">
<title>Morvask Brochure – Cover and Back</title>
<link rel="stylesheet" href="https://fonts.googleapis.com/css2?family=Andika&family=Cabin:wght@400;500&family=Libre+Caslon+Text&display=swap">
<style>
  :root {
    --stage: #d1d2d4;
    --paper: #ffffff;
    --ink: #1a1a1a;
    --label: #111111;
    --accent-pink: #d4457f;
    --photo-light: #f3c48c;
    --photo-deep: #e0974a;
    --band: #0d0d0d;
    --band-text: #ffffff;
  }
  * { margin: 0; padding: 0; box-sizing: border-box; }
  html, body { width: 1200px; height: 848px; overflow: hidden; }
  body { background: var(--stage); position: relative; font-family: "Cabin", sans-serif; color: var(--ink); }

  .panel-label {
    position: absolute; top: 28px; width: 383px; text-align: center;
    font-family: "Cabin", sans-serif; font-size: 42px; font-weight: 400; color: var(--label);
  }
  .panel-label--cover { left: 110px; }
  .panel-label--back { left: 663px; }

  .panel {
    position: absolute; top: 90px; width: 383px; height: 667px;
    background: var(--paper); overflow: hidden;
  }
  .panel--cover { left: 110px; }
  .panel--back { left: 663px; }

  /* Cover */
  .cover-brand {
    position: absolute; left: 12px; top: 50px;
    font-family: "Libre Caslon Text", serif; font-size: 68px; line-height: 1; color: var(--ink);
  }
  .cover-tagline {
    position: absolute; left: 54px; top: 128px;
    font-family: "Cabin", sans-serif; font-size: 22px; letter-spacing: 0.3px; color: var(--ink);
  }
  .cover-photo {
    position: absolute; left: 0; top: 245px; width: 100%; height: 215px;
    background: linear-gradient(180deg, var(--photo-light), var(--photo-deep));
  }
  .cover-band {
    position: absolute; left: 0; bottom: 0; width: 100%; height: 27px;
    background: var(--band); color: var(--band-text);
    font-family: "Cabin", sans-serif; font-size: 17px; letter-spacing: 3px;
    text-align: center; line-height: 27px;
  }

  /* Back */
  .back-brand {
    position: absolute; left: 0; top: 125px; width: 100%;
    display: flex; align-items: center; justify-content: center; gap: 14px;
    font-family: "Cabin", sans-serif; font-size: 58px; font-weight: 500; color: var(--ink);
  }
  .back-brand__mark { width: 22px; height: 22px; background: var(--ink); }
  .mission {
    position: absolute; left: 0; top: 298px; width: 100%; text-align: center;
    font-family: "Andika", sans-serif; font-size: 23px; line-height: 28px; color: var(--accent-pink);
  }
  .contact { position: absolute; left: 16px; top: 484px; list-style: none; }
  .contact__item {
    display: flex; align-items: flex-start; gap: 8px;
    font-family: "Andika", sans-serif; font-size: 20px; line-height: 24px; color: var(--ink);
    margin-bottom: 38px;
  }
  .contact__item:last-child { margin-bottom: 0; }
  .contact__icon { width: 26px; height: 24px; flex: none; }
</style>
</head>
<body>
  <div class="panel-label panel-label--cover">cover</div>
  <div class="panel-label panel-label--back">back</div>

  <section class="panel panel--cover">
    <div class="cover-brand">Morvask</div>
    <div class="cover-tagline">Bringing You Smart Skin Care</div>
    <div class="cover-photo" role="img" aria-label="Photograph of flowing golden-orange silk fabric"></div>
    <div class="cover-band">www.morvask.com</div>
  </section>

  <section class="panel panel--back">
    <div class="back-brand"><span class="back-brand__mark"></span>Morvask</div>
    <p class="mission">Creating Beauty Solutions<br>through Science</p>
    <ul class="contact">
      <li class="contact__item">
        <svg class="contact__icon" viewBox="0 0 26 24" aria-hidden="true">
          <rect x="4" y="2" width="18" height="14" rx="1" fill="none" stroke="var(--accent-pink)" stroke-width="2.2"/>
          <rect x="7" y="5" width="12" height="8" fill="var(--accent-pink)"/>
          <rect x="2" y="18" width="22" height="4" rx="1" fill="var(--accent-pink)"/>
        </svg>
        <span>www.Morvask.com</span>
      </li>
      <li class="contact__item">
        <svg class="contact__icon" viewBox="0 0 26 24" aria-hidden="true">
          <path d="M3 3h20a1 1 0 0 1 1 1v12a1 1 0 0 1-1 1H10l-6 5v-5H3a1 1 0 0 1-1-1V4a1 1 0 0 1 1-1z" fill="none" stroke="var(--accent-pink)" stroke-width="2"/>
          <line x1="7" y1="8" x2="19" y2="8" stroke="var(--accent-pink)" stroke-width="2"/>
          <line x1="7" y1="12" x2="16" y2="12" stroke="var(--accent-pink)" stroke-width="2"/>
        </svg>
        <span>855-555-0147</span>
      </li>
      <li class="contact__item">
        <svg class="contact__icon" viewBox="0 0 26 24" aria-hidden="true">
          <path d="M2 12L13 2l11 10" fill="none" stroke="var(--accent-pink)" stroke-width="2.4" stroke-linejoin="round"/>
          <path d="M5 11v11h6v-6h4v6h6V11" fill="none" stroke="var(--accent-pink)" stroke-width="2.2" stroke-linejoin="round"/>
        </svg>
        <span>1200 Linden Ave.&nbsp; Suite 400<br>Fairview, CA 94000</span>
      </li>
    </ul>
  </section>
</body>
</html>
```